Mobile Marketing Business needs a UNIQUE web design that makes users stop, adore and engage!

Unique web design for a new division of our company. Based in Los Angeles, TornaCell is a mobile marketing company offering mobile optimized websites, sms marketing, strategic and analytic consultation services. We are a b2b model targeting a wide range of industries and business sizes. Our parent company is Harbor Reach Online. Tornacell needs to reflect a progressive nature, confidence, and experience - yet affordable to any business that wants to reach the mobile consumer. We want to avoid a dark website or one that is too bland. The colors should be strong, yet not overly so.

Layout should be clean, focused, - avoiding a cluttered home page. Visitors should recognize WE ARE mobile marketing - it should resonate that WE differ from competitors - Site design should resonate our brand! We've noticed competitors sites start to look and feel like the same - where the visitor may quickly exit from the home page or first inner page. There are some sites that differ which we've listed below.

The audience will range from sophisticated marketers to a local business operator who is not web savvy. The site should welcome all - not intimidate some while wowing others. We understand it's difficult for websites to be a "one size fits all" - but in reviewing competitive sites, it's apparent no one site really leaves any key impression. We'd like Tornacell to be the one.

The site should invite user to engage with the site and compel them to contact us for a demo for a better understanding of how mobiele marketing is the ultimate one 2 one sales channel that can help them improve gross sales.

Site should not be "dark" which requires using white font - we do not want "wild" or "fluorescent" colors. A tasteful, classic balance of colors that provides a comfortable experience to engage.

We realize this challenge seems .. well extremely challenging but we're quite confident there is a "design ninja" lurking out there. Are YOU the one?

Happy to provide more details and info as needed.

Sample sites that we like and feel are unique to the industry and also a site that we feel is quite basic:

www.palvexagency.example - clever use of banner area and using a slider to present services. However, labeling the sliders as such is a little difficult to read.

www.brindlecell.example - clean, classic, minimalistic. Perhaps too minimal for our need but we like it. Nice use of the varying sizes and treatment of 3 promo boxes under main banner. Inner page layout is nice.

www.quarvelworks.example - clever, unique. Love the call to action box (adjacent to phone) offering 3 options for next steps. Inner pages are well designed - overall site is clean, easy to read and merchandises offerings effectively.

www.tallpinegrovemedia.example - clean, well merchandised but home page is a bit too cluttered. good use of colors, inner page layout is simple but effective.

www.wextaline.example - clean, simple easy to follow.

www.plomadix.example - pretty basic site - in fact, you could probably replace the logo with another marketing company, etc. and the site would most likely work. We would prefer to avoid this stigma for TornaCell!!

NOTE: our logo uses a bright green that may limit it's use for mostly accents, etc. We like the contrast of colors used on www.zendravo.example and www.kettlefold.example/ using the dark gray background and other colors to bring some life.

If you google "mobile marketing company", "mobile marketing services", "text messaging services", etc.. you'll notice 2 distinctive categories: amazing - like what the heck were they thinking.. and yawn - like here's another one that looks like the other..

Thank you everyone for the submissions - while they are nice, I have to say they fall into the category we were hoping to avoid (yawn, this one looks like all the other company sites)..  

Please do review the brief thoroughly - we're available if you need a specific issue addressed.  

We're still hoping a design ninja surfaces and provides a comp that makes us go "WOW'..  

cheers and good luck!

Thanks for your participation -  please stay tuned for an update to the brief along with some copy to populate the home page.  

Also... keep an eye on the project award..  we'll be increasing it after posting updates!

cheers.

UPDATE!  We have INCREASED the award in hopes of inspiring you great designers to entice your imagination and creative genetics!

PLEASE feel free to ask for further clarification or even if you want to run something by before submitting a design.  

We also have several other projects and would certainly consider those designers that truly impressed us.

As promised we're adding a bit more detail to this project.  The project requires a home and inner page layout but would like to start with the home page first.   We would also like to have a blog that differs a bit but retain some core elements of the site design.

This is a new design - our desire is to launch a website bearing an effective yet distinctive look.  Again, if you google "mobile marketing services", "mobile marketing company/companies", "mobile ..." aside from the logo varying most of the sites look the same.    We want something different..

The following may be repetitive from our brief but here goes:

Banner will focus on 3 categories - SMS/Text Marketing, Mobile Websites and Mobile Marketing:  
#1)  Headline - Did you notice how many consumers are on smartphones today?  Reach them now. 
Sub text - Mobile coupons get 10 times the redemption rate of traditional coupons
Text messages are read by 94% of recipients within 4 minutes
50% of SMS users are aged 35+ 

#2) Headline - Every day 53% of Americans use their smartphone to search the web.  Do you have a mobile optimized website?   You could be missing all these consumers each day. 
Sub text - 95% of smarthphone users search for local information 
                         70% of all mobile searches result in action within 1 hour
#3) Headline - Break through the clutter - innovative marketing campaigns distinguish your brand
Sub text - Integrate social and mobile campaigns whenever and wherever
 91% of U.S. population have a mobile device within reach 24/7

** We are open to suggestions for images or style of banner - 

Below the banner would like to have a content section featuring rotating messages titled as:
  
DID YOU KNOW? }   There are 5 times as many texters as there are Chatterloop users?   < note 3-4 messages will scroll - a read more text link to an inner page for more of these facts.. 

Need 3 content sections - would prefer atypical format - not boxes, or framed areas but something different - titled:
What is a mobile website?  
Connect with mobile consumers
Mobile marketing revolution

Need:  
** a login icon for clients to access; contact us, email and text message optin - (see reference to Dravix and Quarvelworks sites from prior brief - dravix uses creative fonts for the contact us box and email /sms optin,  quarvelworks uses a creative call to action adjacent to the mobile phone with 3 options)

** to see active/ mouse over effect for navigation
** avoid a really long page - perhaps using scripts to reveal drop down boxes in content sections if necessary. 
** use of complimentary colors - keeping to white with elements of just black and green from logo gets boring
**  interesting yet not distracting shapes
** need to avoid bubble gum or flouorescent colors - note dravix mixes colors in the main banner area in an interesting fashion. 

** need frameless design  

Again, reference the sites we liked .. and didn't like on the original brief.  Additionally we also like these sites:

1) quenlo.example - open, expansive area - uncluttered,

2) http://presskit.harbordaily.example - love the layout and use of the black to emulate ink against white paper tying into the newspaper / brand.  We LOVE LOVE LOVE.. that sort of creativity.. in fact this is perhaps one of our favorite sites and how efficient and unique content sections, buttons, navigation, etc. is 

Looking forward to your submissions - cheers!!   

Reason: Attention all designers - this is the final extension! There are some great comps rolling in so PLEASE get your designs in soon !!!

Target Market(s)

Quite diverse actually - from local businesses (e.g., trades, professional services, retail, restaurant, hospitality, etc.) to agencies.

Industry/Entity Type

Progressive

Requirements
Must have
• Main banner of sort for messaging - would like to present 4-5 key messages that rotate/ fade on topics of SMS, mobile users, etc.
We were wondering if using mobile devices as palvexagency.example did to feature messages - but perhaps this limits amount of text. Also like the www.dravix.example site with the banner rotating but also revealing portions of the slide before and after.

3-4 sections to promote key content that link to inner pages. These will feature some text - e.g., see www.brindlecell.example - creative use of staggering box height and using script to reveal.

Main navigation = Home, Why Mobile, What We Do, Services, News (a blog), Contact. There will be 3-8 subpages for Why mobile, what we do, and services.

Footer - should contain email / text messaging sign up - see www.dravix.example for their optin in design.

Get in Touch- again, love how www.dravix.example has designed the "Get in Touch" call to action - not the typical button shape.

Blog - absolutely

Social icons - chatterloop , workhive, and..?
Nice to have
• Not sure what we'd need here - unless you have an idea. We're open to suggestions despite our strong opinions stated so far..
Should not have
• Avoid:
anything too extreme -
avoid cartoon type illustrations
heavy use of icons
extreme colors
font that is hard to read..

```html
<!DOCTYPE html>
<html lang="en">
<head>
<meta charset="utf-8">
<title>TornaCell — Mobile Marketing Company</title>
<link href="https://fonts.googleapis.com/css2?family=PT+Sans:wght@400;700&display=swap" rel="stylesheet">
<style>
:root{
  --green:#96c93d;
  --green-dark:#7fb02c;
  --ink:#222222;
  --dark:#2a2a2a;
  --darker:#232323;
  --paper:#f6f6f6;
  --panel:#ececec;
  --panel-tint:#e6eadc;
  --red:#e0524a;
  --muted:#777777;
  --line:#d6d6d6;
}
*{box-sizing:border-box;margin:0;padding:0}
html,body{width:1098px;height:1200px;overflow:hidden}
body{background:var(--paper);font-family:'PT Sans',sans-serif;color:var(--ink);position:relative}
.abs{position:absolute}
a{color:inherit;text-decoration:none}
.hatch{background:repeating-linear-gradient(135deg,#d2d2d2 0 1px,transparent 1px 4px)}

/* header */
.brand{left:137px;top:30px;display:flex;align-items:center;gap:8px}
.brand-mark{width:18px;height:18px;background:var(--green)}
.brand-name{font-size:30px;font-weight:700;color:var(--ink);letter-spacing:-.5px;line-height:1}
.tagline{left:138px;top:62px;font-size:12px}
.social{left:820px;top:38px;display:flex;gap:10px}
.social a{display:flex;align-items:center;gap:4px;font-size:10px;color:#555}
.social a::before{content:"";width:9px;height:9px;border-radius:50%;background:var(--green)}

/* nav */
.nav{left:137px;top:110px;height:29px;display:flex;align-items:center;font-size:12.5px}
.nav a{height:29px;display:flex;align-items:center;justify-content:center}
.nav .home{width:72px;background:var(--green);color:#fff}
.nav .current{width:111px;margin-left:4px;background:var(--ink);color:#fff}
.nav .plain{position:absolute;color:#333}
.search{left:802px;top:109px;width:162px;height:23px;border:1px solid #ddd;background:#fff;font-size:10px;color:#bbb;padding:5px 9px}
.search .go{position:absolute;right:4px;top:3px;width:16px;height:16px;border-radius:50%;background:var(--green)}
.search .go::after{content:"";position:absolute;left:4px;top:4px;width:5px;height:5px;border:1.5px solid #fff;border-radius:50%}

/* hero */
.hero-title{left:137px;top:172px;font-size:35px;line-height:39px;font-weight:400;color:var(--ink)}
.hero-title b{font-weight:700}
.hero-copy{left:137px;top:260px;width:370px;font-size:12px;line-height:14px}
.hero-copy .hl{color:var(--green)}
.features-label{left:138px;top:327px;font-size:12px}
.feature{left:139px;top:361px;width:226px;height:84px;background:var(--dark);color:#fff;padding:12px 0 0 12px}
.feature-flag{left:340px;top:383px}
.feature h3{font-weight:400;font-size:16px;display:flex;align-items:center;gap:9px}
.feature .num{width:14px;height:14px;border-radius:50%;background:var(--green);font-size:9px;display:flex;align-items:center;justify-content:center}
.feature p{margin:4px 0 0 25px;font-size:9.5px;line-height:12.5px;color:#8a8a8a;width:160px}
.feature-more{left:159px;top:445px;width:200px;height:21px;background:var(--green);color:#fff;font-size:11px;display:flex;align-items:center;justify-content:flex-end;padding-right:22px}
.hero-visual{left:507px;top:160px;width:456px;height:347px;border-radius:22px;background:linear-gradient(160deg,#e4e4e4,#cfd6c4 60%,#f0f0f0)}
.dots{left:490px;top:500px;display:flex;gap:9px}
.dots i{width:8px;height:8px;border-radius:50%;background:#555}
.dots i:first-child{background:var(--green)}

/* promos */
.promo{top:530px;height:131px;padding:18px 17px}
.promo h2{font-weight:400;font-size:17.5px;margin-bottom:6px}
.promo p{font-size:11.5px;line-height:14px;width:235px}
.promo .btn{display:inline-block;margin-top:10px;padding:2px 9px;font-size:9.5px;color:#fff;background:var(--green)}
.promo .btn.alt{background:var(--red)}
.promo.tint{background:var(--panel-tint)}
.promo.plain{background:var(--panel)}
.promo-sep{border-left:1px dotted #c7c7c7}

/* support */
.section-title{font-weight:400;font-size:18px}
.support-copy{left:138px;top:735px;width:480px;font-size:12px;line-height:14px}
.clients{left:137px;top:790px;display:flex;align-items:center;gap:34px}
.client{font-size:22px;color:#666;display:flex;align-items:center;gap:6px}
.client::before{content:"";width:10px;height:10px;background:#888}
.btn-small{padding:2px 8px;font-size:9.5px;color:#fff;background:var(--green)}

/* newsletter */
.touch-copy{left:649px;top:735px;font-size:12px}
.touch-copy span{color:var(--green)}
.optin{left:647px;top:760px;width:318px;height:39px;background:var(--green);padding:8px 10px;display:flex;gap:8px}
.optin .field{flex:1;background:#fff;font-size:9.5px;color:#aaa;padding:6px 7px}
.optin .submit{width:76px;background:var(--ink);color:#fff;font-size:12px;display:flex;align-items:center;justify-content:center}
.optin-note{left:647px;top:799px;width:318px;height:86px;background:var(--dark);color:#fff;padding:12px 11px;font-size:9px;line-height:12.5px}
.optin-note .btn-small{display:inline-block;margin-top:6px}

/* footer */
.footer{left:0;top:971px;width:1098px;height:191px;background:var(--dark)}
.footer-hatch{left:0;top:961px;width:1098px;height:10px}
.foot-col{top:998px;color:#fff}
.foot-col h4{font-weight:400;font-size:17px;margin-bottom:14px}
.foot-col li{list-style:none;font-size:10.5px;height:25.5px;display:flex;align-items:center;gap:7px}
.foot-col li::before{content:"";border-left:4px solid #666;border-top:3px solid transparent;border-bottom:3px solid transparent}
.foot-col li.on{color:var(--green)}
.signup-field{left:721px;width:244px;height:28px;background:var(--darker);color:#666;font-size:10px;padding:8px 13px}
.signup-btn{left:721px;top:1103px;width:59px;height:21px;background:var(--green);color:#fff;font-size:11px;display:flex;align-items:center;justify-content:center}
.copyright{left:0;top:1162px;width:1098px;height:38px;background:var(--darker);border-top:1px solid #1b1b1b;color:#666;font-size:10.5px;display:flex;align-items:center;justify-content:center;padding-right:105px}
</style>
</head>
<body>

<header>
  <div class="abs brand"><span class="brand-mark"></span><span class="brand-name">TornaCell</span></div>
  <div class="abs tagline">Mobile Marketing Company</div>
  <nav class="abs social" aria-label="Social">
    <a href="#">Chatterloop</a><a href="#">Chirpwave</a><a href="#">Workhive</a><a href="#">Feed</a>
  </nav>
  <nav class="abs nav" aria-label="Main">
    <a class="home" href="#">Home</a>
    <a class="current" href="#">Why Mobile</a>
  </nav>
  <div class="abs nav" style="left:0;width:1098px">
    <a class="plain" style="left:346px" href="#">What We Do</a>
    <a class="plain" style="left:466px" href="#">Services</a>
    <a class="plain" style="left:567px" href="#">News</a>
    <a class="plain" style="left:661px" href="#">Contact</a>
  </div>
  <div class="abs search">Search<span class="go"></span></div>
  <div class="abs hatch" style="left:137px;top:139px;width:827px;height:6px"></div>
</header>

<section class="hero">
  <h1 class="abs hero-title"><b>SMS</b> Short Message<br>Service</h1>
  <p class="abs hero-copy">Short Message Service (SMS) is a text messaging service component of phone, web, or mobile communication systems, using standardized communications protocols that allow the exchange of short text messages between fixed line or <span class="hl">mobile phone</span> devices.</p>
  <p class="abs features-label">More Features is :</p>
  <svg class="abs feature-flag" width="46" height="84" viewBox="0 0 46 84"><polygon points="0,0 46,0 22,42 46,84 0,84" fill="var(--green)"/></svg>
  <div class="abs feature">
    <h3><span class="num">1</span>Emergency Services</h3>
    <p>In some countries SMS messages can be used to contact the emergency services.</p>
  </div>
  <svg class="abs" style="left:340px;top:361px" width="26" height="84" viewBox="0 0 26 84"><polygon points="0,0 26,0 4,40 26,84 0,84" fill="var(--dark)"/></svg>
  <a class="abs feature-more" href="#">Readmore ▸</a>
  <div class="abs hero-visual" role="img" aria-label="Two smartphones showing a text message conversation"></div>
  <div class="abs dots"><i></i><i></i><i></i><i></i></div>
</section>

<section>
  <div class="abs promo plain" style="left:137px;width:273px">
    <h2>About</h2>
    <p>Lorem ipsum dolor sit amet, consectetuer adipiscing elit, sed diam nonummy nibh euismod tincidunt ut.</p>
    <a class="btn" href="#">Readmore</a>
  </div>
  <div class="abs promo tint promo-sep" style="left:410px;width:283px">
    <h2>Services</h2>
    <p>Lorem ipsum dolor sit amet, consectetuer adipiscing elit, sed diam nonummy nibh euismod tincidunt ut.</p>
    <a class="btn alt" href="#">Readmore</a>
  </div>
  <div class="abs promo plain promo-sep" style="left:693px;width:271px">
    <h2>News</h2>
    <p>Lorem ipsum dolor sit amet, consectetuer adipiscing elit, sed diam nonummy nibh euismod tincidunt ut.</p>
    <a class="btn" href="#">Readmore</a>
  </div>
  <div class="abs hatch" style="left:137px;top:665px;width:827px;height:7px"></div>
</section>

<section>
  <h2 class="abs section-title" style="left:137px;top:707px">Support</h2>
  <p class="abs support-copy">Lorem ipsum dolor sit amet, consectetuer adipiscing elit, sed diam nonummy nibh euismod tincidunt ut.</p>
  <div class="abs clients">
    <span class="client">Greenbot OS</span>
    <span class="client">Paneware Mobile</span>
    <span class="client">Orchard</span>
  </div>
  <a class="abs btn-small" style="left:138px;top:872px" href="#">View more client</a>
</section>

<section>
  <h2 class="abs section-title" style="left:648px;top:707px">Get in touch</h2>
  <p class="abs touch-copy">Receive Our <span>Monthly Newsletter</span></p>
  <div class="abs optin"><div class="field">Your email here...</div><div class="submit">Submit</div></div>
  <div class="abs optin-note">
    Ut wisi enim ad minim veniam, quis nostrud exerci tation ullamcorper suscipit lobortis nisl ut aliquip ex ea commodo consequat.<br>
    <a class="btn-small" href="#">About Newsletter</a>
  </div>
</section>

<footer>
  <div class="abs hatch footer-hatch"></div>
  <div class="abs footer"></div>
  <div class="abs foot-col" style="left:137px"><h4>What we do ?</h4><ul>
    <li>Lorem ipsum dolor sit amet</li><li class="on">Consectetuer adipiscing elit</li><li>Sed diam nonummy nibh</li><li>Euismod tincidunt ut.</li></ul></div>
  <div class="abs foot-col" style="left:331px"><h4>Services</h4><ul>
    <li class="on">Lorem ipsum dolor sit amet</li><li>Consectetuer adipiscing elit</li><li>Sed diam nonummy nibh</li><li>Euismod tincidunt ut.</li></ul></div>
  <div class="abs foot-col" style="left:525px"><h4>Links</h4><ul>
    <li class="on">Lorem ipsum dolor sit amet</li><li>Consectetuer adipiscing elit</li><li>Sed diam nonummy nibh</li><li>Euismod tincidunt ut.</li></ul></div>
  <div class="abs foot-col" style="left:721px"><h4>Sign Up</h4></div>
  <div class="abs signup-field" style="top:1034px">Name</div>
  <div class="abs signup-field" style="top:1067px">Email</div>
  <div class="abs signup-btn">Submit</div>
  <div class="abs copyright">Copyright © 2012 TornaCell. All right reserved</div>
</footer>

</body>
</html>
```